Try-fold Brochure for a Dried Fruits and Nuts Retail Shop

Nesrin Bazaar, is a chain of retail shops in Kabul Afghanistan. The business serves high quality dried fruits, Nuts, and a small amount of sweets. The company strive to provide the market (unlike others) a quality product that is graded and sort before packing. Its products are clean, without elements like stones, dusks, or leaves. Nesrin Bazaar is a multi-unit retail that will be supported by a dry fruits and nuts processing plants in the near future. The sign of Nesrin Bazaar is attached. The sign of the parent company Tandem Works & Building Services is attached, however, the wording on the name will be changed to Tandem Works Afghanistan while keeping the circular round logo.

The brochure to focus on the health aspect of dry fruits and nuts along with pictures for Almonds, Walnuts, Pistachios, dry apricots, and raisins for example. The colour scheme to be earth tone colours. Hope this helps. The final product also must allow me to enter texts in Farsi as well as English.
Updates

Greetings everyone, Please see additional notes, description I posted this morning. Good luck and best wishes. Farid

Project Deadline Extended
Reason: The designs in the recent days are getting better. I am also traveling at the moment so an other five days of extension I think would help everyone. Thank you very much for all your submissions so far. I think we are getting near to select an awesome design. Thanks again. Farid

Target Market(s)

Retail markets in Afghanistan, wholesale traders in India, the UAE, Far East for now, Europe/US/Canda markets in three years.

Industry/Entity Type

Retail

Font styles to use
Serif
Sans Serif

Colors
fdf9cf
cadf82
85cae6
fbed23
fde3d4

Requirements
Must have
• It would be good to know that Afghanistan's fruits and nuts are sought after globally and is the rarest, tastiest fruits and nuts in the world. What it lacks is proper processing to include sorting, grading, cleaning and professional packaging. Nesrin Bazaars aim here is to do exactly what this market is missing. Through its processing plant own by its parent company Tandem Works Afghanistan, the company aims to offer the Afghan dry fruits and nuts to the market with all international standards for quality, safety, proper processing and professional packaging at its plant just outside of Kabul, Afghanistan.
Nice to have
• Whenever pictures of nuts used, it would be great to have some benefits of that particular item. For instance, if you have pictures of Almond, the write the benefits of Almonds. I would like to have Almonds, Walnuts, Pistachios, and i.e., dry figs, dried apricots, raisins, etc. When using pictures, I would like them to be transposed in such a way that the covers of the pictures are not visible. Also, please leave one half of one of the folds in the outside for list of addresses and phone numbers of our locations in Kabul, Afghanistan. Currently, there will be five addresses to be entered.

All our stores are designed better than any other retail shop in Kabul. The standard of design and carpentry workmanship is to the same level of quality work one would fine in the US and Europe. Hope this helps.

Elegant, colourful, modern, bold to state a statement of quality.

```html
<!DOCTYPE html>
<html lang="en">
<head>
<meta charset="utf-8">
<title>Nesrin Bazaar – Dried Fruits, Nuts and Sweets</title>
<link href="https://fonts.googleapis.com/css2?family=Tinos:wght@400;700&display=swap" rel="stylesheet">
<style>
  :root {
    --paper: #ffffff;
    --ink: #1f1f1f;
    --brand-blue: #1d5aa5;
    --band-yellow: #f4ec25;
    --row-pink: #fde3d4;
    --row-cream: #fdf9cf;
    --row-green: #cadf82;
    --fold-line: #555555;
    --nut-dark: #7a4a22;
    --nut-mid: #b07840;
    --nut-light: #e2c39a;
    --pistachio: #b9c47a;
    --leaf: #7fae4a;
  }
  * { margin: 0; padding: 0; box-sizing: border-box; }
  html, body { width: 1200px; height: 848px; overflow: hidden; background: var(--paper); }
  .brochure {
    position: relative; width: 1200px; height: 848px; overflow: hidden;
    background: var(--paper); color: var(--ink);
    font-family: "Tinos", "Times New Roman", serif;
  }
  .fold {
    position: absolute; top: 0; width: 0; height: 848px;
    border-left: 1.5px dashed var(--fold-line);
  }
  .fold--first { left: 400px; }
  .fold--second { left: 801px; }

  .product-photo { position: absolute; }
  .product-photo--almonds {
    left: 124px; top: 56px; width: 164px; height: 118px; border-radius: 50%;
    background: radial-gradient(ellipse at 40% 45%, var(--nut-mid), var(--nut-dark) 60%, rgba(122,74,34,0) 72%);
  }
  .product-photo--walnuts {
    left: 96px; top: 460px; width: 208px; height: 140px; border-radius: 45%;
    background: radial-gradient(ellipse at 50% 50%, var(--nut-light), var(--nut-mid) 55%, rgba(176,120,64,0) 72%);
  }
  .product-photo--pistachios {
    left: 892px; top: 46px; width: 204px; height: 132px; border-radius: 50%;
    background: radial-gradient(ellipse at 50% 55%, var(--nut-light), var(--pistachio) 55%, rgba(185,196,122,0) 72%);
  }
  .product-photo--hazelnuts {
    left: 884px; top: 446px; width: 242px; height: 160px; border-radius: 45%;
    background: radial-gradient(ellipse at 45% 55%, var(--nut-mid), var(--nut-dark) 50%, var(--leaf) 65%, rgba(127,174,74,0) 74%);
  }
  .product-photo--mixed {
    left: 500px; top: 296px; width: 200px; height: 200px; border-radius: 50%;
    background: radial-gradient(circle at 50% 50%, var(--nut-light), var(--nut-mid) 55%, var(--nut-dark));
    z-index: 2;
  }

  .benefit-title {
    position: absolute; font-size: 24px; font-weight: 400; letter-spacing: 0.2px;
    white-space: nowrap;
  }
  .benefit-list { position: absolute; list-style: none; }
  .benefit-list li {
    display: flex; align-items: center; justify-content: center;
    height: 39px; font-size: 18.5px; margin-bottom: 5px;
  }
  .benefit-list li:nth-child(1) { background: var(--row-pink); }
  .benefit-list li:nth-child(2) { background: var(--row-cream); }
  .benefit-list li:nth-child(3) { background: var(--row-green); }
  .benefit-list--left { left: 0; width: 400px; }
  .benefit-list--right { left: 802px; width: 398px; }

  .brand {
    position: absolute; left: 420px; top: 36px; width: 360px; height: 86px;
    display: flex; align-items: center; gap: 18px;
  }
  .brand__name {
    font-size: 31px; font-weight: 700; color: var(--brand-blue); white-space: nowrap;
  }
  .brand__dot {
    width: 60px; height: 60px; border-radius: 50%; background: var(--brand-blue); flex: none;
  }
  .tagline {
    position: absolute; left: 400px; top: 190px; width: 401px;
    text-align: center; font-size: 24px; line-height: 35px;
  }
  .accent-band {
    position: absolute; left: 401px; top: 345px; width: 400px; height: 97px;
    background: var(--band-yellow);
  }
  .intro-panel {
    position: absolute; left: 401px; top: 516px; width: 400px; height: 308px;
    background: var(--band-yellow); padding: 14px 18px 0 18px;
  }
  .intro-panel p {
    font-size: 22.5px; line-height: 33px; text-align: justify; hyphens: auto;
    margin-bottom: 22px;
  }
</style>
</head>
<body>
<main class="brochure">
  <div class="fold fold--first"></div>
  <div class="fold fold--second"></div>

  <!-- Almonds -->
  <div class="product-photo product-photo--almonds" role="img" aria-label="Photo of whole almonds with a green leaf"></div>
  <h2 class="benefit-title" style="left:45px; top:205px;">BENEFITS OF ALMONDS:</h2>
  <ul class="benefit-list benefit-list--left" style="top:258px;">
    <li>Lowering cholesterol</li>
    <li>Reducing cancer risk</li>
    <li>Reducing the risk of heart disease</li>
  </ul>

  <!-- Walnuts -->
  <div class="product-photo product-photo--walnuts" role="img" aria-label="Photo of whole and shelled walnuts with leaves"></div>
  <h2 class="benefit-title" style="left:38px; top:642px;">BENEFITS OF WALNUTS:</h2>
  <ul class="benefit-list benefit-list--left" style="top:695px;">
    <li>Helps weight loss</li>
    <li>Prevents diabetes</li>
    <li>Helps you live longer</li>
  </ul>

  <!-- Centre panel -->
  <div class="brand">
    <span class="brand__name">NESRIN BAZAAR</span>
    <span class="brand__dot" aria-hidden="true"></span>
  </div>
  <p class="tagline">Provider of Dried Fruits,<br>Nuts and Sweets</p>
  <div class="accent-band"></div>
  <div class="product-photo product-photo--mixed" role="img" aria-label="Photo of a round heap of mixed nuts: cashews, almonds, pecans, hazelnuts and peanuts"></div>
  <section class="intro-panel">
    <p>"Lorem ipsum dolor sit amet, consectetur adipiscing elit, sed do eiusmod tempor incididunt ut labore et dolore magna aliqua. Ut</p>
    <p>"Lorem ipsum dolor sit amet, consectetur adipiscing elit, sed do eiusmod tempor incididunt ut labore et dolore magna aliqua. Ut</p>
  </section>

  <!-- Pistachios -->
  <div class="product-photo product-photo--pistachios" role="img" aria-label="Photo of pistachios in their shells with leaves"></div>
  <h2 class="benefit-title" style="left:833px; top:210px;">BENEFITS OF PISTACHIOS:</h2>
  <ul class="benefit-list benefit-list--right" style="top:265px;">
    <li>Boosts immunity</li>
    <li>Maintains Skin Health</li>
    <li>Stimulates Hair Growth</li>
  </ul>

  <!-- Hazelnuts -->
  <div class="product-photo product-photo--hazelnuts" role="img" aria-label="Photo of hazelnuts with green leaves"></div>
  <h2 class="benefit-title" style="left:832px; top:637px;">BENEFITS OF HAZELNUTS:</h2>
  <ul class="benefit-list benefit-list--right" style="top:697px;">
    <li>High in B vitamins</li>
    <li>Protects nervous system</li>
    <li>Strengthens digestive tract health</li>
  </ul>
</main>
</body>
</html>
```